Licensed School Psychologist Business Card Design (may be single or double sided)

In an empathetic and nurturing environment, I conduct comprehensive psycho-educational evaluations for children and adolescents who may be experiencing academic, social/emotional challenges, and stressors in their lives. Given the collection of data and information, recommendations, supports, and strategies are created and tailored to the strengths and weaknesses of the children/adolescents as well as their families.

Industry/Entity Type

Business

Contact Information for Business Card

Bright-Path Learning Assessments
Helen Marchetti, MEd; MA
Licensed School Psychologist
482 Tolliver Lane, Suite #3
Larkfield, OR 97412
P: 555 612-3094 F: 555 612-3157

```html
<!DOCTYPE html>
<html lang="en">
<head>
<meta charset="utf-8">
<title>Bright-Path Learning Assessments – Business Card</title>
<link rel="stylesheet" href="https://fonts.googleapis.com/css2?family=Marcellus+SC&family=Ubuntu:wght@300;400&display=swap">
<style>
  :root {
    --backdrop: #ece9e3;
    --card-white: #fdfdfd;
    --lime: #a9cd2e;
    --lime-light: #c8de4a;
    --lime-dark: #93bb1f;
    --ink-grey: #8d8d8d;
    --ink-soft: #a5a5a5;
  }
  * { box-sizing: border-box; margin: 0; padding: 0; }
  html, body { width: 1200px; height: 885px; overflow: hidden; }
  body {
    background: var(--backdrop);
    font-family: "Ubuntu", sans-serif;
    position: relative;
  }
  .card {
    position: absolute;
    width: 620px;
    height: 354px;
    border-radius: 18px;
    box-shadow: 0 10px 28px rgba(0,0,0,.18);
    overflow: hidden;
  }
  /* Front */
  .card-front {
    left: 70px; top: 70px;
    background: var(--card-white);
  }
  .holder {
    position: absolute; right: 44px; top: 36px;
    text-align: right;
  }
  .holder-name {
    font-family: "Marcellus SC", serif;
    color: var(--lime);
    font-size: 30px;
    letter-spacing: .5px;
  }
  .holder-degrees {
    color: var(--ink-soft);
    font-weight: 300;
    font-size: 19px;
    margin-top: 2px;
  }
  .holder-title {
    color: var(--ink-soft);
    font-weight: 300;
    font-size: 20px;
    margin-top: 4px;
  }
  .divider {
    position: absolute;
    left: 195px; right: 44px; top: 178px;
    height: 2px; background: var(--lime-light);
  }
  .brand-front {
    position: absolute; left: 34px; top: 116px;
    width: 150px;
    display: flex; flex-direction: column; align-items: center; gap: 10px;
  }
  .brand-mark {
    width: 70px; height: 70px; border-radius: 50%;
    background: #e6efc4;
  }
  .brand-name {
    font-family: "Marcellus SC", serif;
    color: var(--ink-grey);
    font-size: 15px;
    line-height: 1.2;
    text-align: center;
  }
  .contact-phones {
    position: absolute; left: 44px; bottom: 34px;
    list-style: none;
    color: var(--ink-soft);
    font-size: 21px; font-weight: 300;
  }
  .contact-phones li { display: flex; align-items: center; gap: 10px; margin-top: 4px; }
  .contact-phones svg { width: 20px; height: 20px; }
  .contact-address {
    position: absolute; right: 44px; bottom: 34px;
    text-align: right;
    color: var(--ink-soft);
    font-size: 20px; font-weight: 300;
    font-style: normal; line-height: 1.45;
  }
  /* Back */
  .card-back {
    left: 510px; top: 462px;
    background: radial-gradient(ellipse at 60% 70%, var(--lime-light) 0%, var(--lime) 60%, var(--lime-dark) 100%);
    display: flex; align-items: center; justify-content: center; gap: 22px;
  }
  .card-back .brand-mark {
    width: 96px; height: 96px;
    background: none; border: 3px solid #fff;
  }
  .card-back .brand-name {
    color: #fff; font-size: 28px; text-align: left; line-height: 1.25;
  }
</style>
</head>
<body>
  <section class="card card-front" aria-label="Business card front">
    <div class="holder">
      <div class="holder-name">Helen Marchetti</div>
      <div class="holder-degrees">MEd; MA</div>
      <div class="holder-title">Licensed School Psychologist</div>
    </div>
    <div class="divider"></div>
    <div class="brand-front">
      <div class="brand-mark"></div>
      <div class="brand-name">Bright-Path<br>Learning Assessments</div>
    </div>
    <ul class="contact-phones">
      <li>
        <svg viewBox="0 0 20 20" aria-hidden="true"><rect width="20" height="20" rx="3" fill="#a9cd2e"/><path d="M6 5c1 0 2 2 2 3s-1 1-1 1.5 2 3 3.5 3.5c.5 0 .5-1 1.5-1s3 1 3 2-1 2-2 2C9 16 4 11 4 7c0-1 1-2 2-2z" fill="#fff"/></svg>
        555 612-3094
      </li>
      <li>
        <svg viewBox="0 0 20 20" aria-hidden="true"><rect width="20" height="20" rx="3" fill="#a9cd2e"/><rect x="5" y="4" width="10" height="5" fill="#fff"/><rect x="4" y="9" width="12" height="7" rx="1" fill="#fff"/><rect x="6" y="11" width="8" height="1.5" fill="#a9cd2e"/></svg>
        555 612-3157
      </li>
    </ul>
    <address class="contact-address">
      482 Tolliver Lane<br>
      Suite #3 Larkfield, OR 97412
    </address>
  </section>

  <section class="card card-back" aria-label="Business card back">
    <div class="brand-mark"></div>
    <div class="brand-name">Bright-Path<br>Learning Assessments</div>
  </section>
</body>
</html>
```